BRIVETTA Need a luxury modern business card designed.

Need a luxury modern business card designed. refer to the uploaded files for the company name and logo in the zip file under source files. i will making my descion on monday. so please send in before then so if we need to edit we will have the time. we have a trade show coming up and im on a deadline for printer.

Target Market(s)

high end clients

Contact Information for Business Card

Company nAme and logo. Calvin Moross Co-Founder / Project Manager Office # 416-555-7391 Cell # 416-555-0186 BRIVETTA.CA Calvin@brivetta.ca

Font styles to use
Other font styles liked:
• Modern

Requirements
Must have
• Company name and logo, contact info, using the black, gold and white color scheme.

```html
<!DOCTYPE html>
<html lang="en">
<head>
<meta charset="utf-8">
<title>BRIVETTA – Business Card</title>
<link href="https://fonts.googleapis.com/css2?family=Poppins:wght@300;400;500;600&display=swap" rel="stylesheet">
<style>
  :root {
    --stage: #2a2a2b;
    --card-white: #ffffff;
    --charcoal: #323232;
    --ink: #2b2b2b;
    --gold: #a89660;
    --soft-grey: #9a9a9a;
    --line-grey: #bdbdbd;
  }
  * { box-sizing: border-box; margin: 0; padding: 0; }
  html, body {
    width: 1200px; height: 880px; overflow: hidden;
    background: var(--stage);
    font-family: "Poppins", sans-serif;
  }
  .canvas { position: relative; width: 1200px; height: 880px; }

  .card {
    position: absolute;
    background: var(--card-white);
    border-radius: 18px;
    overflow: hidden;
    box-shadow: 0 18px 40px rgba(0,0,0,0.45);
  }

  /* Front */
  .card-front { left: 90px; top: 280px; width: 580px; height: 331px; }
  .front-wordmark {
    position: absolute; left: 0; right: 0; top: 138px;
    display: flex; align-items: center; justify-content: center; gap: 16px;
  }
  .wordmark {
    font-weight: 300; color: var(--ink);
    letter-spacing: 0.16em; font-size: 44px; line-height: 1;
  }
  .wordmark-square { width: 16px; height: 16px; background: var(--gold); }

  /* Back */
  .card-back { left: 760px; top: 140px; width: 340px; height: 595px; }
  .card-back svg.back-shapes { position: absolute; inset: 0; }
  .back-wordmark {
    position: absolute; left: 0; right: 0; top: 92px;
    display: flex; align-items: center; justify-content: center; gap: 12px;
  }
  .back-wordmark .wordmark { font-size: 32px; }
  .back-wordmark .wordmark-square { width: 12px; height: 12px; }

  .person { position: absolute; left: 36px; top: 298px; }
  .person-name {
    font-weight: 500; font-size: 23px; letter-spacing: 0.02em; color: #fff;
    text-transform: uppercase;
  }
  .person-name .surname { color: var(--gold); }
  .person-title { font-size: 14px; color: var(--soft-grey); font-weight: 400; margin-top: 2px; }

  .contact { position: absolute; left: 36px; right: 28px; }
  .contact-phone { top: 392px; }
  .contact-mail { top: 446px; }
  .contact-row { display: flex; align-items: center; gap: 10px; }
  .icon {
    width: 26px; height: 26px; border-radius: 50%;
    border: 2px solid #fff; display: flex; align-items: center; justify-content: center;
    flex: none;
  }
  .contact-text { color: #fff; font-size: 13.5px; font-weight: 400; white-space: nowrap; }
  .contact-rule { height: 1px; background: var(--line-grey); opacity: 0.6; margin-top: 10px; width: 80%; }

  .website {
    position: absolute; left: 0; right: 0; bottom: 0; height: 62px;
    display: flex; align-items: center; justify-content: center;
    color: #fff; font-weight: 600; font-size: 17px; letter-spacing: 0.22em;
  }
</style>
</head>
<body>
<main class="canvas">

  <section class="card card-front" aria-label="Business card front">
    <div class="front-wordmark">
      <span class="wordmark-square"></span>
      <span class="wordmark">BRIVETTA</span>
    </div>
  </section>

  <section class="card card-back" aria-label="Business card back">
    <svg class="back-shapes" width="340" height="595" viewBox="0 0 340 595">
      <path d="M0 200 Q 190 210 340 330 L340 595 L0 595 Z" fill="var(--gold)"/>
      <path d="M0 212 Q 185 222 340 346 L340 595 L0 595 Z" fill="var(--charcoal)"/>
      <path d="M40 226 Q 200 240 330 352" fill="none" stroke="#fff" stroke-width="2.5"/>
      <rect x="0" y="527" width="340" height="6" fill="#fff"/>
      <rect x="0" y="533" width="340" height="62" fill="var(--gold)"/>
    </svg>

    <div class="back-wordmark">
      <span class="wordmark-square"></span>
      <span class="wordmark">BRIVETTA</span>
    </div>

    <div class="person">
      <p class="person-name">Calvin <span class="surname">Moross</span></p>
      <p class="person-title">Co-Founder / Project Manager</p>
    </div>

    <div class="contact contact-phone">
      <div class="contact-row">
        <span class="icon">
          <svg width="14" height="14" viewBox="0 0 24 24"><path fill="#fff" d="M6.6 10.8a15.1 15.1 0 0 0 6.6 6.6l2.2-2.2a1 1 0 0 1 1-.25 11.4 11.4 0 0 0 3.6.6 1 1 0 0 1 1 1V20a1 1 0 0 1-1 1A17 17 0 0 1 3 4a1 1 0 0 1 1-1h3.5a1 1 0 0 1 1 1c0 1.25.2 2.45.6 3.6a1 1 0 0 1-.25 1z"/></svg>
        </span>
        <span class="icon">
          <svg width="12" height="14" viewBox="0 0 12 16"><rect x="1.5" y="1" width="9" height="14" rx="1.5" fill="none" stroke="#fff" stroke-width="1.6"/><circle cx="6" cy="12.5" r="0.9" fill="#fff"/></svg>
        </span>
        <span class="contact-text">416-555-7391 / 416-555-0186</span>
      </div>
      <div class="contact-rule"></div>
    </div>

    <div class="contact contact-mail">
      <div class="contact-row">
        <span class="icon">
          <svg width="14" height="11" viewBox="0 0 16 12"><rect x="1" y="1" width="14" height="10" fill="none" stroke="#fff" stroke-width="1.5"/><path d="M1 1 L8 7 L15 1" fill="none" stroke="#fff" stroke-width="1.5"/></svg>
        </span>
        <span class="contact-text">Calvin@brivetta.ca</span>
      </div>
      <div class="contact-rule"></div>
    </div>

    <p class="website">BRIVETTA.CA</p>
  </section>

</main>
</body>
</html>
```